PowerPoint template designs for my business

LumaPath is an educational services company that provides consulting and strategic planning services for Christian schools. We regularly produce webinars and other in-person presentations and would like our own PowerPoint templates to use for these presentations. We are looking for Master Slides and themes which incorporate our corporate image. See our logo and color palate in the uploaded files.

```html
<!DOCTYPE html>
<html lang="en">
<head>
<meta charset="utf-8">
<title>LumaPath Presentation Template</title>
<link href="https://fonts.googleapis.com/css2?family=Roboto:wght@400;500;700;900&display=swap" rel="stylesheet">
<style>
:root{
  --navy:#2b3a4b;
  --navy-dark:#223040;
  --maroon:#7b1c22;
  --maroon-dark:#5f1419;
  --canvas:#d8d8d8;
  --ink:#1f2630;
  --muted:#8b9098;
  --line:#d9dce0;
  --soft:#eef0f2;
  --photo-a:#9aa0a7;
  --photo-b:#6f757d;
  --photo-warm:#b49a86;
  --white:#ffffff;
}
*{box-sizing:border-box;margin:0;padding:0}
html,body{width:1200px;height:938px;overflow:hidden}
body{background:var(--canvas);font-family:"Roboto",Arial,sans-serif;color:var(--ink)}
.deck{display:grid;grid-template-columns:repeat(5,206px);column-gap:24px;row-gap:35px;padding:32px 37px}
.slide{position:relative;width:206px;height:116px;background:var(--white);overflow:hidden;box-shadow:0 1px 2px rgba(0,0,0,.12)}
.slide.navy{background:var(--navy)}
.slide svg.bg{position:absolute;inset:0;width:206px;height:116px}
.abs{position:absolute}
.photo{background:linear-gradient(135deg,var(--photo-a),var(--photo-b))}
.photo.warm{background:linear-gradient(135deg,#c9b29c,#8d7766)}
.photo.light{background:linear-gradient(135deg,#d7dadd,#aeb3b9)}
.photo.dark{background:linear-gradient(135deg,#5d646d,#3a4048)}
.title{position:absolute;top:6px;left:8px;font-size:6px;font-weight:700;color:var(--ink);white-space:nowrap}
.title em{font-style:normal;color:var(--maroon)}
.logo{position:absolute;top:5px;right:8px;font-size:6.5px;font-weight:500;color:var(--navy);letter-spacing:.1px}
.logo.light{color:var(--white)}
.foot{position:absolute;left:0;right:0;bottom:0;height:8px}
.foot span{position:absolute;bottom:3px;font-size:2.6px;color:var(--muted)}
.foot .conf{left:8px}
.foot .page{right:8px}
.foot::after{content:"";position:absolute;left:0;right:0;bottom:0;height:2px;background:linear-gradient(90deg,var(--maroon) 0 30%,var(--navy) 30%)}
.txt{font-size:2.7px;line-height:1.45;color:var(--muted)}
.txt.w{color:#d4d9df}
.h{font-size:4.2px;font-weight:700;line-height:1.2;color:var(--ink)}
.h.w{color:var(--white)}
.big{font-size:9px;font-weight:700;line-height:1.15;color:var(--white)}
.stat{font-size:8px;font-weight:700;line-height:1}
.box{position:absolute}
.bg-maroon{background:var(--maroon)}
.bg-navy{background:var(--navy)}
.bg-soft{background:var(--soft)}
.circle{position:absolute;border-radius:50%}
.icon{position:absolute;width:9px;height:9px;border-radius:50%;border:.8px solid var(--maroon);background:var(--white)}
.pill{position:absolute;background:var(--maroon);color:var(--white);font-size:2.8px;padding:1.5px 4px}
table.data{position:absolute;border-collapse:collapse;font-size:2.5px;color:var(--ink)}
table.data td,table.data th{border-bottom:.4px solid var(--line);padding:1.2px 2px;text-align:left;font-weight:400}
table.data tr.hl td{background:var(--maroon);color:var(--white)}
table.data th{background:var(--navy);color:var(--white);font-weight:500}
</style>
</head>
<body>
<main class="deck">

<!-- row 1 -->
<section class="slide navy">
  <svg class="bg" viewBox="0 0 206 116">
    <polygon points="118,0 206,0 206,116 96,116" fill="#8d939a" role="img" aria-label="Photo of a teacher presenting to a class"/>
    <polygon points="108,0 118,0 96,116 86,116" fill="#7b1c22"/>
  </svg>
  <div class="logo light" style="left:10px;right:auto;top:14px;font-size:8px">LumaPath</div>
  <div class="abs big" style="left:10px;top:52px;font-size:7.5px">Presentation Title Here</div>
  <div class="abs txt w" style="left:10px;top:63px;width:70px">Lorem ipsum dolor sit amet, consectetur</div>
  <div class="pill" style="left:10px;top:82px">Dec 2026</div>
</section>

<section class="slide navy">
  <svg class="bg" viewBox="0 0 206 116">
    <polygon points="130,0 206,0 206,116 100,116" fill="#a59584" role="img" aria-label="Photo of a person writing in a notebook"/>
    <polygon points="150,116 206,70 206,116" fill="#7b1c22"/>
  </svg>
  <div class="logo light" style="left:10px;right:auto;top:14px;font-size:8px">LumaPath</div>
  <div class="abs big" style="left:10px;top:52px;font-size:7.5px">Presentation Title Here</div>
  <div class="abs txt w" style="left:10px;top:63px;width:70px">Lorem ipsum dolor sit amet, consectetur</div>
  <div class="pill" style="left:10px;top:82px">Dec 2026</div>
</section>

<section class="slide">
  <div class="abs photo dark" style="left:0;top:0;width:62px;height:116px" role="img" aria-label="Photo of a laptop on a desk"></div>
  <div class="box bg-maroon" style="left:62px;top:0;width:4px;height:116px"></div>
  <div class="abs h w" style="left:8px;top:26px;font-size:5px">Agenda</div>
  <div class="abs txt w" style="left:8px;top:34px;width:48px">Lorem ipsum dolor sit amet, consectetur adipiscing elit.</div>
  <div class="logo" style="color:var(--maroon)">LumaPath</div>
  <div class="abs txt" style="left:74px;top:22px;width:80px;line-height:3.1">— Lorem ipsum dolor sit amet<br>— Consectetur adipiscing elit<br>— Maecenas porttitor congue<br>— Fusce posuere magna sed<br>— Pulvinar ultricies purus<br>— Lectus malesuada libero<br>— Sit amet commodo magna</div>
</section>

<section class="slide">
  <div class="box bg-navy" style="left:0;top:0;width:206px;height:50px"></div>
  <div class="abs txt w" style="left:40px;top:12px;width:126px;text-align:center">Lorem ipsum dolor sit amet, ne periculis repudiare dissentiunt, est ad duis dicunt delicata. Quo ne veniam dissentias ut.</div>
  <div class="circle photo" style="left:88px;top:34px;width:30px;height:30px;border:1.5px solid #fff" role="img" aria-label="Portrait photo of a school leader"></div>
  <div class="abs h" style="left:0;right:0;top:70px;text-align:center;font-size:4px;font-weight:500;letter-spacing:.3px">WELCOME MESSAGE</div>
  <div class="box bg-maroon" style="left:97px;top:76px;width:12px;height:1px"></div>
</section>

<section class="slide">
  <svg class="bg" viewBox="0 0 206 116">
    <rect width="206" height="116" fill="#a28a78" role="img" aria-label="Photo of wooden stairs"/>
    <polygon points="110,0 206,0 206,116 148,116" fill="#2b3a4b"/>
    <polygon points="100,0 110,0 148,116 138,116" fill="#7b1c22"/>
  </svg>
  <div class="abs h w" style="right:8px;top:26px;font-size:5px">Slide Title Here</div>
  <div class="abs txt w" style="right:8px;top:34px;width:74px;text-align:right">Lorem ipsum dolor sit amet, consectetur adipiscing elit. Maecenas porttitor congue massa.</div>
  <div class="abs txt w" style="right:8px;top:64px;width:60px;text-align:right">Fusce posuere, magna sed pulvinar ultricies, purus lectus malesuada libero.</div>
</section>

<!-- row 2 -->
<section class="slide">
  <svg class="bg" viewBox="0 0 206 116">
    <polygon points="110,14 206,14 206,90 90,90" fill="#8f959c" role="img" aria-label="Photo of students working at a table"/>
    <polygon points="90,90 110,14 124,14 104,90" fill="#2b3a4b"/>
  </svg>
  <div class="title">Slide <em>Title</em> Here</div><div class="logo">LumaPath</div>
  <div class="abs h" style="left:8px;top:20px;width:70px">Lorem ipsum dolor sit amet, consectetur adipiscing elit. Maecenas porttitor congue massa.</div>
  <div class="abs txt" style="left:8px;top:40px;width:70px">Fusce posuere, magna sed pulvinar ultricies, purus lectus malesuada libero, sit amet commodo magna eros quis urna.</div>
  <div class="abs stat" style="left:8px;top:78px;color:var(--maroon)">01</div>
  <div class="abs txt" style="left:22px;top:78px;width:26px">Lorem ipsum dolor sit amet elit</div>
  <div class="abs stat" style="left:54px;top:78px;color:var(--maroon)">02</div>
  <div class="abs txt" style="left:68px;top:78px;width:26px">Lorem ipsum dolor sit amet elit</div>
  <div class="foot"><span class="conf">Confidential and not for distribution</span><span class="page">Page 10</span></div>
</section>

<section class="slide">
  <svg class="bg" viewBox="0 0 206 116">
    <polygon points="150,14 206,14 206,100 128,100" fill="#a0a6ad" role="img" aria-label="Photo of a hand writing on sticky notes"/>
    <polygon points="128,100 150,14 160,14 150,60 138,100" fill="#2b3a4b"/>
  </svg>
  <div class="title" style="top:7px"></div><div class="logo">LumaPath</div>
  <div class="box bg-maroon" style="left:8px;top:22px;width:50px;height:30px"></div>
  <div class="abs stat" style="left:11px;top:25px;color:#fff">10,000+</div>
  <div class="abs txt w" style="left:11px;top:36px;width:44px">Lorem ipsum dolor sit amet consectetur</div>
  <div class="abs stat" style="left:64px;top:25px;color:var(--navy)">10,000+</div>
  <div class="abs txt" style="left:64px;top:36px;width:44px">Lorem ipsum dolor sit amet consectetur</div>
  <div class="abs stat" style="left:11px;top:60px;color:var(--navy)">10,000+</div>
  <div class="abs txt" style="left:11px;top:71px;width:44px">Lorem ipsum dolor sit amet consectetur</div>
  <div class="box bg-maroon" style="left:61px;top:57px;width:50px;height:30px"></div>
  <div class="abs stat" style="left:64px;top:60px;color:#fff">10,000+</div>
  <div class="abs txt w" style="left:64px;top:71px;width:44px">Lorem ipsum dolor sit amet consectetur</div>
  <div class="foot"><span class="conf">Confidential and not for distribution</span><span class="page">Page 11</span></div>
</section>

<section class="slide">
  <svg class="bg" viewBox="0 0 206 116">
    <rect x="80" y="0" width="126" height="108" fill="#9ba1a8" role="img" aria-label="Photo of a team meeting in an office"/>
    <polygon points="0,0 130,0 96,108 0,108" fill="#7b1c22"/>
  </svg>
  <div class="title" style="color:#fff">Slide Title Here</div><div class="logo light">LumaPath</div>
  <div class="abs h w" style="left:8px;top:22px;width:80px">Lorem ipsum dolor sit amet, consectetur adipiscing elit. Maecenas porttitor congue massa.</div>
  <div class="abs txt w" style="left:8px;top:44px;width:80px">Fusce posuere, magna sed pulvinar ultricies, purus lectus malesuada libero, sit amet commodo magna eros quis urna. Nunc viverra imperdiet enim.</div>
  <div class="foot"><span class="conf">Confidential and not for distribution</span><span class="page">Page 12</span></div>
</section>

<section class="slide">
  <div class="abs photo" style="left:0;top:0;width:100px;height:108px" role="img" aria-label="Photo of a laptop in a bright office"></div>
  <div class="box bg-maroon" style="left:90px;top:14px;width:116px;height:94px"></div>
  <div class="abs txt w" style="left:98px;top:22px">Your Sub-Title Here</div>
  <div class="abs big" style="left:98px;top:32px">Your Title<br>Here</div>
  <div class="abs txt w" style="left:98px;top:58px;width:90px">Lorem ipsum dolor sit amet, consectetur adipiscing elit. Maecenas porttitor congue massa. Fusce posuere, magna sed pulvinar ultricies.</div>
  <div class="logo">LumaPath</div>
  <div class="foot"><span class="conf">Confidential and not for distribution</span><span class="page">Page 13</span></div>
</section>

<section class="slide">
  <div class="title">Slide <em>Title</em> Here</div><div class="logo">LumaPath</div>
  <div class="abs photo light" style="left:8px;top:16px;width:190px;height:34px" role="img" aria-label="Photo of a bright workspace"></div>
  <div class="box bg-maroon" style="left:8px;top:26px;width:62px;height:48px"></div>
  <div class="abs h w" style="left:12px;top:30px">Your Title Here</div>
  <div class="abs txt w" style="left:12px;top:38px;width:54px">Lorem ipsum dolor sit amet, consectetur adipiscing elit. Maecenas porttitor.</div>
  <div class="icon" style="left:90px;top:54px"></div><div class="icon" style="left:126px;top:54px"></div><div class="icon" style="left:162px;top:54px"></div>
  <div class="abs stat" style="left:80px;top:70px;color:var(--navy);font-size:5.5px">10,000+</div>
  <div class="abs stat" style="left:116px;top:70px;color:var(--navy);font-size:5.5px">10,000+</div>
  <div class="abs stat" style="left:152px;top:70px;color:var(--navy);font-size:5.5px">10,000+</div>
  <div class="abs txt" style="left:80px;top:78px;width:110px;word-spacing:8px">Lorem&nbsp;ipsum Dolor&nbsp;sit Amet&nbsp;elit</div>
  <div class="foot"><span class="conf">Confidential and not for distribution</span><span class="page">Page 14</span></div>
</section>

<!-- row 3 -->
<section class="slide">
  <div class="title">Slide <em>Title</em> Here</div><div class="logo">LumaPath</div>
  <div class="abs photo warm" style="left:112px;top:14px;width:94px;height:94px" role="img" aria-label="Photo of a smiling educator"></div>
  <div class="box bg-soft" style="left:8px;top:22px;width:46px;height:34px"></div>
  <div class="box bg-soft" style="left:60px;top:22px;width:46px;height:34px"></div>
  <div class="icon" style="left:26px;top:25px"></div><div class="icon" style="left:78px;top:25px"></div>
  <div class="abs txt" style="left:11px;top:37px;width:40px;text-align:center">Lorem ipsum dolor sit amet adipiscing</div>
  <div class="abs txt" style="left:63px;top:37px;width:40px;text-align:center">Lorem ipsum dolor sit amet adipiscing</div>
  <div class="box bg-soft" style="left:8px;top:62px;width:46px;height:34px"></div>
  <div class="box bg-soft" style="left:60px;top:62px;width:46px;height:34px"></div>
  <div class="icon" style="left:26px;top:65px"></div><div class="icon" style="left:78px;top:65px"></div>
  <div class="abs txt" style="left:11px;top:77px;width:40px;text-align:center">Lorem ipsum dolor sit amet adipiscing</div>
  <div class="abs txt" style="left:63px;top:77px;width:40px;text-align:center">Lorem ipsum dolor sit amet adipiscing</div>
  <div class="foot"><span class="conf">Confidential and not for distribution</span><span class="page">Page 15</span></div>
</section>

<section class="slide">
  <div class="title">Slide <em>Title</em> Here</div><div class="logo">LumaPath</div>
  <div class="abs photo warm" style="left:8px;top:16px;width:48px;height:40px" role="img" aria-label="Photo of a desk with a laptop"></div>
  <div class="box bg-navy" style="left:58px;top:16px;width:48px;height:40px"></div>
  <div class="box bg-maroon" style="left:108px;top:16px;width:48px;height:40px"></div>
  <div class="abs photo" style="left:158px;top:16px;width:40px;height:40px" role="img" aria-label="Photo of a smiling educator"></div>
  <div class="box bg-navy" style="left:8px;top:58px;width:48px;height:40px"></div>
  <div class="abs photo" style="left:58px;top:58px;width:98px;height:40px" role="img" aria-label="Photo of a person at a whiteboard"></div>
  <div class="box bg-soft" style="left:158px;top:58px;width:40px;height:40px"></div>
  <div class="abs txt w" style="left:61px;top:22px;width:42px">Lorem ipsum dolor sit amet, consectetur adipiscing elit.</div>
  <div class="abs txt w" style="left:11px;top:64px;width:42px">Lorem ipsum dolor sit amet, consectetur adipiscing elit.</div>
  <div class="abs txt" style="left:161px;top:64px;width:34px">Lorem ipsum dolor sit amet elit.</div>
  <div class="foot"><span class="conf">Confidential and not for distribution</span><span class="page">Page 16</span></div>
</section>

<section class="slide">
  <div class="title">Slide <em>Title</em> Here</div><div class="logo">LumaPath</div>
  <div class="abs photo warm" style="left:8px;top:18px;width:44px;height:30px" role="img" aria-label="Photo of hands on a laptop"></div>
  <div class="abs photo" style="left:56px;top:18px;width:44px;height:30px" role="img" aria-label="Photo of a notebook"></div>
  <div class="abs photo light" style="left:104px;top:18px;width:44px;height:30px" role="img" aria-label="Photo of a smiling educator"></div>
  <div class="abs photo warm" style="left:152px;top:18px;width:46px;height:30px" role="img" aria-label="Photo of a classroom"></div>
  <div class="box bg-navy" style="left:8px;top:48px;width:44px;height:7px"></div><div class="box bg-navy" style="left:56px;top:48px;width:44px;height:7px"></div><div class="box bg-maroon" style="left:104px;top:48px;width:44px;height:7px"></div><div class="box bg-navy" style="left:152px;top:48px;width:46px;height:7px"></div>
  <div class="abs txt" style="left:8px;top:62px;width:190px">Lorem ipsum dolor sit amet, consectetur adipiscing elit. Maecenas porttitor congue massa. Fusce posuere, magna sed pulvinar ultricies, purus lectus malesuada libero, sit amet commodo magna eros quis urna. Nunc viverra imperdiet enim.</div>
  <div class="foot"><span class="conf">Confidential and not for distribution</span><span class="page">Page 17</span></div>
</section>

<section class="slide">
  <div class="title">Slide <em>Title</em> Here</div><div class="logo">LumaPath</div>
  <div class="box bg-navy" style="left:0;top:36px;width:206px;height:50px"></div>
  <div class="abs photo warm" style="left:78px;top:14px;width:52px;height:94px" role="img" aria-label="Photo of a smiling educator"></div>
  <div class="box bg-maroon" style="left:64px;top:14px;width:14px;height:22px"></div>
  <div class="icon" style="left:64px;top:44px"></div><div class="icon" style="left:64px;top:64px"></div>
  <div class="icon" style="left:134px;top:44px"></div><div class="icon" style="left:134px;top:64px"></div>
  <div class="abs txt w" style="left:8px;top:42px;width:52px">Lorem ipsum dolor sit amet, consectetur adipiscing elit.</div>
  <div class="abs txt w" style="left:8px;top:62px;width:52px">Lorem ipsum dolor sit amet, consectetur adipiscing elit.</div>
  <div class="abs txt w" style="left:148px;top:42px;width:50px">Lorem ipsum dolor sit amet, consectetur adipiscing elit.</div>
  <div class="abs txt w" style="left:148px;top:62px;width:50px">Lorem ipsum dolor sit amet, consectetur adipiscing elit.</div>
  <div class="foot"><span class="conf">Confidential and not for distribution</span><span class="page">Page 18</span></div>
</section>

<section class="slide">
  <div class="title">Slide <em>Title</em> Here</div><div class="logo">LumaPath</div>
  <div class="abs txt" style="left:8px;top:16px;width:80px">Lorem ipsum dolor sit amet, consectetur adipiscing elit. Maecenas porttitor congue massa.</div>
  <div class="icon" style="left:10px;top:34px"></div><div class="icon" style="left:48px;top:34px"></div>
  <div class="abs txt" style="left:6px;top:45px;width:34px">Lorem ipsum dolor sit amet</div>
  <div class="abs txt" style="left:44px;top:45px;width:34px">Lorem ipsum dolor sit amet</div>
  <div class="icon" style="left:10px;top:62px"></div><div class="icon" style="left:48px;top:62px"></div>
  <div class="abs txt" style="left:6px;top:73px;width:34px">Lorem ipsum dolor sit amet</div>
  <div class="abs txt" style="left:44px;top:73px;width:34px">Lorem ipsum dolor sit amet</div>
  <div class="abs" style="left:104px;top:18px;width:94px;height:84px;background:radial-gradient(circle at 50% 55%,#c7d6ea,#f2f5f9 70%)" role="img" aria-label="Illustration of people working around a large laptop"></div>
  <div class="foot"><span class="conf">Confidential and not for distribution</span><span class="page">Page 19</span></div>
</section>

<!-- row 4 -->
<section class="slide">
  <div class="abs photo dark" style="left:0;top:0;width:206px;height:44px" role="img" aria-label="Photo of a stairway"></div>
  <div class="abs" style="left:8px;top:22px;width:70px;height:64px;background:radial-gradient(circle,#c7d6ea,#eef2f7 70%)" role="img" aria-label="Illustration of a person at a large laptop"></div>
  <div class="abs h w" style="left:96px;top:28px;font-size:5px">PRESENTATION</div>
  <div class="abs txt" style="left:96px;top:48px;width:100px">Lorem ipsum dolor sit amet, consectetur adipiscing elit. Maecenas porttitor congue massa.</div>
  <div class="box bg-navy" style="left:96px;top:64px;width:12px;height:10px"></div>
  <div class="box bg-maroon" style="left:124px;top:64px;width:12px;height:10px"></div>
  <div class="box bg-navy" style="left:152px;top:64px;width:12px;height:10px"></div>
  <div class="abs txt" style="left:90px;top:77px;width:110px;word-spacing:9px">Lorem&nbsp;ipsum Dolor&nbsp;sit Amet&nbsp;elit</div>
  <div class="foot"><span class="conf">Confidential and not for distribution</span><span class="page">Page 20</span></div>
</section>

<section class="slide">
  <div class="title">Slide <em>Title</em> Here</div><div class="logo">LumaPath</div>
  <div class="box bg-soft" style="left:0;top:48px;width:206px;height:52px"></div>
  <div class="abs photo light" style="left:8px;top:18px;width:62px;height:70px" role="img" aria-label="Photo of a laptop on a desk"></div>
  <div class="abs txt" style="left:80px;top:18px;width:116px">Lorem ipsum dolor sit amet, consectetur adipiscing elit. Maecenas porttitor congue massa. Fusce posuere, magna sed pulvinar ultricies, purus lectus malesuada libero.</div>
  <div class="icon" style="left:92px;top:56px"></div><div class="icon" style="left:122px;top:56px"></div><div class="icon" style="left:152px;top:56px"></div><div class="icon" style="left:182px;top:56px"></div>
  <div class="abs txt" style="left:84px;top:68px;width:116px;word-spacing:7px">Lorem&nbsp;ipsum Dolor&nbsp;sit Amet&nbsp;elit Magna&nbsp;sed</div>
  <div class="foot"><span class="conf">Confidential and not for distribution</span><span class="page">Page 21</span></div>
</section>

<section class="slide">
  <div class="box bg-soft" style="left:8px;top:18px;width:44px;height:66px"></div>
  <div class="circle photo" style="left:16px;top:24px;width:28px;height:28px" role="img" aria-label="Portrait photo of a consultant"></div>
  <div class="abs h" style="left:8px;top:58px;width:44px;text-align:center;font-size:3.4px">Daniel Reyes</div>
  <div class="abs txt" style="left:8px;top:63px;width:44px;text-align:center">Lead Consultant</div>
  <div class="box bg-navy" style="left:58px;top:18px;width:68px;height:66px"></div>
  <div class="box bg-navy" style="left:130px;top:18px;width:68px;height:66px"></div>
  <div class="abs h w" style="left:62px;top:22px">About Daniel</div>
  <div class="abs h w" style="left:134px;top:22px">About Us</div>
  <div class="abs txt w" style="left:62px;top:30px;width:60px">Lorem ipsum dolor sit amet, consectetur adipiscing elit. Maecenas porttitor congue massa. Fusce posuere, magna sed pulvinar ultricies.</div>
  <div class="abs txt w" style="left:134px;top:30px;width:60px">Lorem ipsum dolor sit amet, consectetur adipiscing elit. Maecenas porttitor congue massa. Fusce posuere, magna sed pulvinar ultricies.</div>
  <div class="circle bg-maroon" style="left:10px;top:91px;width:4px;height:4px"></div><div class="abs txt" style="left:16px;top:91px">hello@lumapath.org</div>
  <div class="circle bg-maroon" style="left:60px;top:91px;width:4px;height:4px"></div><div class="abs txt" style="left:66px;top:91px">+1 (555) 014 2290</div>
  <div class="circle bg-maroon" style="left:112px;top:91px;width:4px;height:4px"></div><div class="abs txt" style="left:118px;top:91px">www.lumapath.org</div>
  <div class="circle bg-maroon" style="left:162px;top:91px;width:4px;height:4px"></div><div class="abs txt" style="left:168px;top:91px">@lumapath</div>
  <div class="foot"><span class="conf">Confidential and not for distribution</span><span class="page">Page 22</span></div>
</section>

<section class="slide">
  <div class="title">Slide <em>Title</em> Here</div><div class="logo">LumaPath</div>
  <svg class="bg" viewBox="0 0 206 116">
    <polygon points="8,30 62,30 62,104 8,104" fill="#eef0f2"/><polygon points="8,70 16,70 16,104 8,104" fill="#7b1c22"/>
    <polygon points="74,30 128,30 128,104 74,104" fill="#eef0f2"/><polygon points="74,70 82,70 82,104 74,104" fill="#7b1c22"/>
    <polygon points="140,30 194,30 194,104 140,104" fill="#eef0f2"/><polygon points="140,70 148,70 148,104 140,104" fill="#7b1c22"/>
  </svg>
  <div class="circle photo" style="left:29px;top:18px;width:12px;height:12px" role="img" aria-label="Portrait photo of a team member"></div>
  <div class="circle photo" style="left:95px;top:18px;width:12px;height:12px" role="img" aria-label="Portrait photo of a team member"></div>
  <div class="circle photo" style="left:161px;top:18px;width:12px;height:12px" role="img" aria-label="Portrait photo of a team member"></div>
  <div class="abs h" style="left:8px;top:33px;width:54px;text-align:center;font-size:3.2px">Daniel Reyes</div>
  <div class="abs h" style="left:74px;top:33px;width:54px;text-align:center;font-size:3.2px">Daniel Reyes</div>
  <div class="abs h" style="left:140px;top:33px;width:54px;text-align:center;font-size:3.2px">Daniel Reyes</div>
  <div class="abs txt" style="left:20px;top:40px;width:40px">Lorem ipsum dolor sit amet, consectetur adipiscing elit. Maecenas porttitor congue.</div>
  <div class="abs txt" style="left:86px;top:40px;width:40px">Lorem ipsum dolor sit amet, consectetur adipiscing elit. Maecenas porttitor congue.</div>
  <div class="abs txt" style="left:152px;top:40px;width:40px">Lorem ipsum dolor sit amet, consectetur adipiscing elit. Maecenas porttitor congue.</div>
  <div class="foot"><span class="conf">Confidential and not for distribution</span><span class="page">Page 23</span></div>
</section>

<section class="slide navy">
  <div class="abs photo dark" style="left:0;top:0;width:206px;height:116px;opacity:.5" role="img" aria-label="Faint photo of a city skyline"></div>
  <div class="abs stat" style="left:10px;top:20px;color:#fff">10,000+</div>
  <div class="abs txt w" style="left:10px;top:30px;width:60px">Lorem ipsum dolor sit amet</div>
  <div class="abs stat" style="left:10px;top:44px;color:#fff">10,000+</div>
  <div class="abs txt w" style="left:10px;top:54px;width:60px">Lorem ipsum dolor sit amet</div>
  <div class="abs stat" style="left:10px;top:68px;color:#fff">10,000+</div>
  <div class="abs txt w" style="left:10px;top:78px;width:60px">Lorem ipsum dolor sit amet</div>
  <div class="abs h w" style="left:96px;top:20px;font-size:5px">Slide With Number Sample</div>
  <div class="abs txt w" style="left:96px;top:30px;width:100px">Lorem ipsum dolor sit amet, consectetur adipiscing elit. Maecenas porttitor congue massa. Fusce posuere, magna sed pulvinar ultricies, purus lectus malesuada libero, sit amet commodo magna eros quis urna. Nunc viverra imperdiet enim.</div>
  <div class="abs txt w" style="left:96px;top:60px;width:100px">Pellentesque habitant morbi tristique senectus et netus et malesuada fames ac turpis egestas.</div>
</section>

<!-- row 5 -->
<section class="slide">
  <div class="title">Table <em>Sample</em> Slide</div><div class="logo">LumaPath</div>
  <div class="abs txt" style="left:8px;top:15px;width:190px">There are many variations of passages of Lorem Ipsum available, but the majority have suffered alteration in some form, by injected humour, or randomised words which don't look even slightly believable.</div>
  <table class="data" style="left:8px;top:32px;width:190px">
    <tr><th>Program</th><th>Number</th><th>Text Here</th></tr>
    <tr class="hl"><td>Lorem ipsum</td><td>1,000</td><td>Text</td></tr>
    <tr><td>Dolor sit</td><td>2,500</td><td>Text</td></tr>
    <tr><td>Amet elit</td><td>1,200</td><td>Text</td></tr>
    <tr class="hl"><td>Magna sed</td><td>3,400</td><td>Text</td></tr>
    <tr><td>Porttitor</td><td>800</td><td>Text</td></tr>
    <tr><td>Congue massa</td><td>1,750</td><td>Text</td></tr>
    <tr><td>Total</td><td>10,650</td><td>Text</td></tr>
  </table>
  <div class="foot"><span class="conf">Confidential and not for distribution</span><span class="page">Page 25</span></div>
</section>

<section class="slide">
  <div class="title">Infographics <em>Sample</em> Slide</div><div class="logo">LumaPath</div>
  <div class="abs txt" style="left:8px;top:15px;width:190px">Lorem ipsum dolor sit amet, consectetur adipiscing elit. Maecenas porttitor congue massa.</div>
  <div class="box bg-soft" style="left:8px;top:26px;width:54px;height:56px"></div><div class="box bg-maroon" style="left:8px;top:26px;width:54px;height:7px"></div>
  <div class="box bg-soft" style="left:76px;top:26px;width:54px;height:56px"></div><div class="box bg-maroon" style="left:76px;top:26px;width:54px;height:7px"></div>
  <div class="box bg-soft" style="left:144px;top:26px;width:54px;height:56px"></div><div class="box bg-maroon" style="left:144px;top:26px;width:54px;height:7px"></div>
  <div class="abs txt w" style="left:12px;top:27px">Your Title Here</div><div class="abs txt w" style="left:80px;top:27px">Your Title Here</div><div class="abs txt w" style="left:148px;top:27px">Your Title Here</div>
  <div class="abs txt" style="left:11px;top:36px;width:48px">Lorem ipsum dolor sit amet, consectetur adipiscing elit. Maecenas porttitor congue massa fusce posuere.</div>
  <div class="abs txt" style="left:79px;top:36px;width:48px">Lorem ipsum dolor sit amet, consectetur adipiscing elit. Maecenas porttitor congue massa fusce posuere.</div>
  <div class="abs txt" style="left:147px;top:36px;width:48px">Lorem ipsum dolor sit amet, consectetur adipiscing elit. Maecenas porttitor congue massa fusce posuere.</div>
  <svg class="bg" viewBox="0 0 206 116"><path d="M66,52 L71,56 L66,60" fill="none" stroke="#2b3a4b" stroke-width="1.2"/><path d="M134,52 L139,56 L134,60" fill="none" stroke="#2b3a4b" stroke-width="1.2"/></svg>
  <div class="box bg-maroon" style="left:8px;top:86px;width:190px;height:12px"></div>
  <div class="circle" style="left:10px;top:88px;width:8px;height:8px;background:#fff"></div>
  <div class="abs txt w" style="left:22px;top:88px;width:170px">Lorem ipsum dolor sit amet, consectetur adipiscing elit. Maecenas porttitor congue massa.</div>
  <div class="foot"><span class="conf">Confidential and not for distribution</span><span class="page">Page 26</span></div>
</section>

<section class="slide">
  <div class="title">Infographics <em>Sample</em> Slide</div><div class="logo">LumaPath</div>
  <div class="box bg-maroon" style="left:40px;top:18px;width:70px;height:7px"></div>
  <div class="box bg-maroon" style="left:114px;top:18px;width:70px;height:7px"></div>
  <div class="abs txt w" style="left:58px;top:19px">Your Title Here</div><div class="abs txt w" style="left:132px;top:19px">Your Title Here</div>
  <div class="box bg-navy" style="left:10px;top:28px;width:8px;height:34px"></div>
  <div class="box bg-navy" style="left:10px;top:64px;width:8px;height:34px"></div>
  <div class="box bg-soft" style="left:20px;top:28px;width:14px;height:70px"></div>
  <div class="abs txt" style="left:40px;top:30px;width:70px;line-height:2.3">• Lorem ipsum dolor sit amet<br>• Consectetur adipiscing elit<br>• Maecenas porttitor congue<br>• Fusce posuere magna sed<br>• Pulvinar ultricies purus<br>• Lectus malesuada libero<br>• Sit amet commodo magna</div>
  <div class="box bg-soft" style="left:114px;top:28px;width:70px;height:70px"></div>
  <div class="abs txt" style="left:118px;top:30px;width:64px;line-height:2.3">Lorem ipsum dolor sit amet<br>Consectetur adipiscing elit<br>Maecenas porttitor congue<br>Fusce posuere magna sed<br>Pulvinar ultricies purus<br>Lectus malesuada libero<br>Sit amet commodo magna</div>
  <div class="foot"><span class="conf">Confidential and not for distribution</span><span class="page">Page 27</span></div>
</section>

<section class="slide">
  <div class="title">Slide <em>Title</em> Here</div><div class="logo">LumaPath</div>
  <div class="box bg-navy" style="left:8px;top:24px;width:88px;height:30px"></div>
  <div class="box bg-maroon" style="left:110px;top:24px;width:88px;height:30px"></div>
  <div class="box bg-maroon" style="left:8px;top:60px;width:88px;height:30px"></div>
  <div class="box bg-navy" style="left:110px;top:60px;width:88px;height:30px"></div>
  <div class="circle" style="left:93px;top:31px;width:20px;height:16px;background:#fff;border:.8px solid var(--line)"></div>
  <div class="circle" style="left:93px;top:67px;width:20px;height:16px;background:#fff;border:.8px solid var(--line)"></div>
  <div class="abs h w" style="left:12px;top:28px;font-size:3.2px">Lorem ipsum dolor sit amet</div>
  <div class="abs txt w" style="left:12px;top:34px;width:74px">Lorem ipsum dolor sit amet, consectetur adipiscing elit. Maecenas porttitor.</div>
  <div class="abs h w" style="left:118px;top:28px;font-size:3.2px">Lorem ipsum dolor sit amet</div>
  <div class="abs txt w" style="left:118px;top:34px;width:74px">Lorem ipsum dolor sit amet, consectetur adipiscing elit. Maecenas porttitor.</div>
  <div class="abs h w" style="left:12px;top:64px;font-size:3.2px">Lorem ipsum dolor sit amet</div>
  <div class="abs txt w" style="left:12px;top:70px;width:74px">Lorem ipsum dolor sit amet, consectetur adipiscing elit. Maecenas porttitor.</div>
  <div class="abs h w" style="left:118px;top:64px;font-size:3.2px">Lorem ipsum dolor sit amet</div>
  <div class="abs txt w" style="left:118px;top:70px;width:74px">Lorem ipsum dolor sit amet, consectetur adipiscing elit. Maecenas porttitor.</div>
  <div class="foot"><span class="conf">Confidential and not for distribution</span><span class="page">Page 28</span></div>
</section>

<section class="slide">
  <div class="title">Infographics <em>Sample</em> Slide</div><div class="logo">LumaPath</div>
  <div class="box bg-navy" style="left:8px;top:18px;width:34px;height:8px"></div>
  <div class="box bg-navy" style="left:46px;top:18px;width:34px;height:8px"></div>
  <div class="box bg-navy" style="left:84px;top:18px;width:34px;height:8px"></div>
  <div class="box bg-maroon" style="left:122px;top:18px;width:34px;height:8px"></div>
  <div class="box bg-navy" style="left:160px;top:18px;width:38px;height:8px"></div>
  <div class="abs txt w" style="left:8px;top:19.5px;width:190px;word-spacing:14px">Your&nbsp;Title Your&nbsp;Title Your&nbsp;Title Your&nbsp;Title Your&nbsp;Title</div>
  <div class="abs txt" style="left:10px;top:30px;width:30px">• Lorem ipsum<br>• Dolor sit amet<br>• Consectetur<br>• Adipiscing<br>• Maecenas</div>
  <div class="abs txt" style="left:48px;top:30px;width:30px">• Lorem ipsum<br>• Dolor sit amet<br>• Consectetur<br>• Adipiscing<br>• Maecenas</div>
  <div class="abs txt" style="left:86px;top:30px;width:30px">• Lorem ipsum<br>• Dolor sit amet<br>• Consectetur<br>• Adipiscing<br>• Maecenas</div>
  <div class="abs txt" style="left:124px;top:30px;width:30px">• Lorem ipsum<br>• Dolor sit amet<br>• Consectetur<br>• Adipiscing<br>• Maecenas</div>
  <div class="abs txt" style="left:162px;top:30px;width:34px">• Lorem ipsum<br>• Dolor sit amet<br>• Consectetur<br>• Adipiscing<br>• Maecenas</div>
  <svg class="bg" viewBox="0 0 206 116">
    <line x1="8" y1="80" x2="198" y2="80" stroke="#2b3a4b" stroke-width=".6"/>
    <g fill="#7b1c22"><path d="M36,78 l4,2 l-4,2z"/><path d="M74,78 l4,2 l-4,2z"/><path d="M112,78 l4,2 l-4,2z"/><path d="M150,78 l4,2 l-4,2z"/></g>
  </svg>
  <div class="abs txt" style="left:14px;top:83px;width:186px;word-spacing:26px">01 02 03 04 05</div>
  <div class="foot"><span class="conf">Confidential and not for distribution</span><span class="page">Page 29</span></div>
</section>

<!-- row 6 -->
<section class="slide">
  <div class="title">Infographics <em>Sample</em> Slide</div><div class="logo">LumaPath</div>
  <svg class="bg" viewBox="0 0 206 116">
    <path d="M40,98 Q80,90 106,62 Q120,48 134,42 L131,36 L150,40 L138,54 L136,48 Q124,54 112,68 Q86,98 40,104 Z" fill="#2b3a4b"/>
    <circle cx="66" cy="93" r="4" fill="#7b1c22"/><circle cx="90" cy="80" r="4" fill="#7b1c22"/><circle cx="108" cy="64" r="4" fill="#7b1c22"/><circle cx="126" cy="50" r="4" fill="#7b1c22"/>
    <g stroke="#9aa0a7" stroke-width=".4"><line x1="66" y1="89" x2="66" y2="70"/><line x1="90" y1="76" x2="90" y2="28"/><line x1="108" y1="68" x2="108" y2="92"/><line x1="126" y1="54" x2="126" y2="80"/></g>
  </svg>
  <div class="abs txt" style="left:36px;top:62px;width:40px">Lorem ipsum dolor sit amet</div>
  <div class="abs txt" style="left:70px;top:20px;width:40px"><b style="color:var(--maroon)">Your Title</b><br>Lorem ipsum dolor sit amet</div>
  <div class="abs txt" style="left:112px;top:88px;width:40px">Lorem ipsum dolor sit amet</div>
  <div class="abs txt" style="left:130px;top:76px;width:40px">Lorem ipsum dolor sit amet</div>
  <div class="foot"><span class="conf">Confidential and not for distribution</span><span class="page">Page 30</span></div>
</section>

<section class="slide">
  <div class="title">Chart <em>Slide</em> Sample</div><div class="logo">LumaPath</div>
  <div class="box bg-soft" style="left:8px;top:18px;width:70px;height:70px"></div>
  <svg class="abs" style="left:18px;top:24px" width="50" height="50" viewBox="0 0 50 50">
    <circle cx="25" cy="25" r="17" fill="none" stroke="#2b3a4b" stroke-width="10" stroke-dasharray="48 107" transform="rotate(-90 25 25)"/>
    <circle cx="25" cy="25" r="17" fill="none" stroke="#7b1c22" stroke-width="10" stroke-dasharray="32 107" stroke-dashoffset="-48" transform="rotate(-90 25 25)"/>
    <circle cx="25" cy="25" r="17" fill="none" stroke="#a7acb2" stroke-width="10" stroke-dasharray="17 107" stroke-dashoffset="-80" transform="rotate(-90 25 25)"/>
    <circle cx="25" cy="25" r="17" fill="none" stroke="#dfe2e5" stroke-width="10" stroke-dasharray="10 107" stroke-dashoffset="-97" transform="rotate(-90 25 25)"/>
  </svg>
  <div class="box bg-maroon" style="left:8px;top:88px;width:70px;height:10px"></div>
  <div class="abs txt w" style="left:11px;top:89px;width:64px">Lorem ipsum dolor sit amet elit.</div>
  <div class="box" style="left:84px;top:18px;width:114px;height:80px;border:.5px solid var(--line)"></div>
  <div class="abs h" style="left:88px;top:24px;font-size:3.2px;line-height:5.6">First<br>Analysis<br>First<br>Analysis<br>First<br>Analysis<br>First<br>Analysis</div>
  <div class="abs txt" style="left:116px;top:24px;width:78px;line-height:3.73">Lorem ipsum dolor sit amet, consectetur adipiscing elit. Maecenas porttitor congue massa. Fusce posuere, magna sed pulvinar ultricies, purus lectus malesuada libero, sit amet commodo.</div>
  <div class="foot"><span class="conf">Confidential and not for distribution</span><span class="page">Page 31</span></div>
</section>

<section class="slide navy">
  <div class="logo light" style="left:12px;right:auto;top:14px;font-size:8px">LumaPath</div>
  <div class="abs big" style="left:12px;top:80px;font-size:9px">Slide Break</div>
  <div class="abs txt w" style="left:12px;top:92px;width:70px">Lorem ipsum dolor sit amet, consectetur adipiscing elit.</div>
</section>

<section class="slide">
  <div class="title">Blank <em>Slide</em> Sample</div><div class="logo">LumaPath</div>
  <div class="foot"><span class="conf">Confidential and not for distribution</span><span class="page">Page 33</span></div>
</section>

<section class="slide">
  <div class="abs photo dark" style="left:0;top:0;width:206px;height:116px" role="img" aria-label="Photo of hands typing on a keyboard"></div>
  <div class="box bg-maroon" style="left:0;top:0;width:78px;height:116px;opacity:.92"></div>
  <div class="abs h w" style="left:8px;top:10px;font-size:5px">CONTACT US</div>
  <div class="abs txt w" style="left:8px;top:20px;width:64px">Lorem ipsum dolor sit amet, consectetur adipiscing elit. Maecenas porttitor congue massa. Fusce posuere, magna sed pulvinar ultricies.</div>
  <div class="abs txt w" style="left:8px;top:68px;line-height:2.6">● 12 Grove Lane, Springfield<br>● +1 (555) 014 2290<br>● www.lumapath.org<br>● hello@lumapath.org</div>
  <div class="abs" style="left:110px;top:44px;font-size:14px;font-weight:500;color:#fff">LumaPath</div>
  <div class="abs txt w" style="left:111px;top:62px">Educational Consulting &amp; Strategic Planning</div>
</section>

</main>
</body>
</html>
```